Gravel Ale Label design/Graphic design

The Company
Gravel ale is an exciting new brand of ‘fit beer’ targeted at fitness enthusiasts as well as beer lovers. Gravel ale is a craft beer with added protein which can be used as a post work out recovery/leisure beverage. The target audience is generally male, 18-30 years old.
We need label/graphic design of the product to appear on our website www.gravelale-demo.co.uk

The Project
The project is to submit four designs, one for each flavour:
• Larger
• Honey Ale
• Banana Ale
• Zero Alcohol

The design of each flavour must be differentiated, yet have a consistent theme throughout all flavours. At this point Gravel ale has no official logo so feel free to incorporate this into the design, although this is not absolutely necessary.

The label/design should include the following basic information:
Brand name: Gravel Ale
Type: Larger/Honey Ale/Banana Ale/Zero
Tag: 7g High Quality Protein
Alcohol percentage: 4%/Vol (0%/Vol for the Zero alcohol version)
Volume: 300ml

Brand Guidelines (designs not necessarily limited to these)
Font: Aldrich
Main Colours: Blue # 005fbf Orange # ed7000
Basic beer bottle image attached.

The final design will be displayed on (but not limited to) the website www.gravelale-demo.co.uk

The winning designer may be contacted for future projects and opportunities with Gravel Ale.
Updates

Project Deadline Extended
Reason: My apologies I have been sick the last few days and have been unable to provide feedback. Your work is much appreciated, I will extend the project to give us a little more time and provide feedback individually later today. Best Regards, Oliver

Target Market(s)

The target audience is generally male, 18-30 years old.

Industry/Entity Type

Fitness

Requirements
Must have
• The label/design should include the following basic information:
Brand name: Gravel Ale
Volume: 300ml

```html
<!DOCTYPE html>
<html lang="en">
<head>
<meta charset="utf-8">
<title>Gravel Ale – Craft Beer Labels</title>
<link href="https://fonts.googleapis.com/css2?family=Russo+One&family=Roboto:wght@400;500&display=swap" rel="stylesheet">
<style>
  :root {
    --bg: #e3e5ed;
    --label: #fbfaf6;
    --ink: #141414;
    --tag: #e8890f;
    --banana: #d6d40f;
    --zero: #16204a;
    --larger: #1b1b1b;
    --honey: #c9471b;
    --band-text: #ffffff;
  }
  * { margin: 0; padding: 0; box-sizing: border-box; }
  html, body { width: 1200px; height: 800px; overflow: hidden; }
  body { background: var(--bg); font-family: "Roboto", Arial, sans-serif; }

  .range {
    position: relative;
    width: 1200px;
    height: 800px;
    display: flex;
    justify-content: center;
    align-items: center;
    gap: 54px;
  }

  .label {
    width: 216px;
    height: 320px;
    background: var(--label);
    display: flex;
    flex-direction: column;
    align-items: center;
    box-shadow: 0 2px 6px rgba(0,0,0,0.08);
  }

  .brand-mark {
    margin-top: 22px;
    width: 46px;
    height: 46px;
    border-radius: 50%;
    background: var(--tag);
  }

  .brand-name {
    margin-top: 10px;
    font-family: "Russo One", sans-serif;
    font-size: 31px;
    line-height: 1;
    color: var(--ink);
    letter-spacing: 0.5px;
  }

  .brand-sub {
    margin-top: 4px;
    font-family: "Russo One", sans-serif;
    font-size: 15px;
    letter-spacing: 1.5px;
    color: var(--ink);
  }

  .flavour {
    margin-top: 14px;
    width: 112px;
    padding: 3px 0 2px;
    background: var(--tag);
    color: #fff;
    text-align: center;
    font-family: "Russo One", sans-serif;
    font-size: 13px;
    letter-spacing: 0.5px;
  }

  .protein {
    margin-top: 10px;
    font-size: 13px;
    line-height: 1.2;
    text-align: center;
    color: #333;
  }

  .facts {
    margin-top: auto;
    margin-bottom: 38px;
    width: 100%;
    height: 40px;
    display: flex;
    align-items: center;
    color: var(--band-text);
    font-size: 12px;
  }
  .facts span {
    flex: 1;
    text-align: center;
  }
  .facts span + span { border-left: 1px solid rgba(255,255,255,0.7); }

  .label--banana .facts { background: var(--banana); }
  .label--zero .facts { background: var(--zero); }
  .label--larger .facts { background: var(--larger); }
  .label--honey .facts { background: var(--honey); }
</style>
</head>
<body>
  <main class="range">
    <article class="label label--banana">
      <div class="brand-mark"></div>
      <h1 class="brand-name">GRAVEL ALE</h1>
      <p class="brand-sub">CRAFT BEER</p>
      <p class="flavour">BANANA ALE</p>
      <p class="protein">7g High<br>Quality Protein</p>
      <div class="facts"><span>4%vol</span><span>300ml</span></div>
    </article>

    <article class="label label--zero">
      <div class="brand-mark"></div>
      <h1 class="brand-name">GRAVEL ALE</h1>
      <p class="brand-sub">CRAFT BEER</p>
      <p class="flavour">ZERO</p>
      <p class="protein">7g High<br>Quality Protein</p>
      <div class="facts"><span>4%vol</span><span>300ml</span></div>
    </article>

    <article class="label label--larger">
      <div class="brand-mark"></div>
      <h1 class="brand-name">GRAVEL ALE</h1>
      <p class="brand-sub">CRAFT BEER</p>
      <p class="flavour">LARGER</p>
      <p class="protein">7g High<br>Quality Protein</p>
      <div class="facts"><span>4%vol</span><span>300ml</span></div>
    </article>

    <article class="label label--honey">
      <div class="brand-mark"></div>
      <h1 class="brand-name">GRAVEL ALE</h1>
      <p class="brand-sub">CRAFT BEER</p>
      <p class="flavour">HONEY ALE</p>
      <p class="protein">7g High<br>Quality Protein</p>
      <div class="facts"><span>4%vol</span><span>300ml</span></div>
    </article>
  </main>
</body>
</html>
```